Fennick Executive Search - New Business Card Design Project

We are an executive search firm called Fennick Executive Search based in the UK. We require a custom design for a business card. We're looking to convey a professional service to executives for executive search recruitment services. In terms of colours, we like dark blues and grays (maybe even silver incorporated somewhere if we go for a foiled type of card) but we're open to your artistic flare. See our current logo in attachments. We are totally open on design so long as the design is slick and professional.
Updates

Thanks for all your contributions of various designs. I have to say the quality of work has been amazing which is going to make our job quite difficult in the coming days on making a decision. Thanks to you all that have taken the time to submit designs thus far. We'll keep on reviewing and try to narrow down our selection as soon as possible.

Target Market(s)

Executive Search

Industry/Entity Type

Recruitment

Contact Information for Business Card

Fennick Executive Search,
Connecting Boards with Exceptional Leadership
Gordon Pellbury, Managing Director,
07823 906417
0117 486 7132
gordon@fennickexecutive.co.uk
fennickexecutive.co.uk
58 Lindmoor Court, Hatherley Road, Bristol, BS32 9QJ

Font styles to use
Sans Serif
Other font styles liked:
• Roboto (which is used in our logo)

Requirements
Must have
• Our logo (It has a subtle fade on it from #02071d at top to #333649 at bottom)
• The logo can be on one side or both sides
• Must be elegant and professional
• We have 2nd slogan ADVISE | ENGAGE | ELEVATE | ACHIEVE which can be incorporated into the card
Nice to have
• Use of blues and grey colours
• Compatible with similar styling to our website fennickexecutive.co.uk
Should not have
• Must not be overly brash
• Must not contain cartoon characters

```html
<!DOCTYPE html>
<html lang="en">
<head>
<meta charset="utf-8">
<title>Fennick Executive Search – Business Card</title>
<link rel="stylesheet" href="https://fonts.googleapis.com/css2?family=Roboto:wght@400;500;700&family=Tinos&display=swap">
<style>
  :root {
    --backdrop: #9c9a93;
    --card-white: #ffffff;
    --band-grey: #71717a;
    --navy: #0b1128;
    --navy-soft: #333649;
    --text-grey: #55555c;
    --text-light: #f2f2f4;
  }
  * { margin: 0; padding: 0; box-sizing: border-box; }
  html, body {
    width: 1200px; height: 1200px; overflow: hidden;
    background: var(--backdrop);
    font-family: "Roboto", Arial, sans-serif;
  }
  .card {
    position: absolute;
    width: 768px; height: 482px;
    background: var(--card-white);
    overflow: hidden;
  }
  .card--front { left: 54px; top: 78px; }
  .card--back { left: 335px; top: 658px; }
  .card__bands { position: absolute; inset: 0; }
  .card__bands polygon { fill: var(--band-grey); }

  .brand { position: absolute; display: flex; align-items: center; }
  .brand__square { background: linear-gradient(#02071d, var(--navy-soft)); flex: none; }
  .brand__name { color: var(--navy); font-weight: 500; white-space: nowrap; }
  .card--front .brand { left: 39px; top: 72px; gap: 10px; }
  .card--front .brand__square { width: 34px; height: 34px; }
  .card--front .brand__name { font-size: 17px; }
  .card--back .brand { left: 321px; top: 248px; gap: 12px; }
  .card--back .brand__square { width: 40px; height: 40px; }
  .card--back .brand__name { font-size: 21px; }

  .holder { position: absolute; left: 515px; top: 40px; }
  .holder__name { font-size: 21.5px; font-weight: 500; color: var(--text-light); }
  .holder__surname { color: var(--navy); }
  .holder__role { font-size: 12px; color: var(--text-light); margin-top: 6px; }

  .tagline-diagonal {
    position: absolute; left: 66px; top: 238px;
    transform: rotate(-31deg); transform-origin: left bottom;
    font-size: 11px; line-height: 15px; color: var(--text-grey);
    white-space: nowrap;
  }

  .contacts { position: absolute; left: 227px; top: 255px; list-style: none; }
  .contacts__item { display: flex; align-items: center; height: 22px; margin-bottom: 22px; }
  .contacts__badge {
    width: 22px; height: 22px; border-radius: 50%;
    background: var(--navy); color: #fff;
    font-size: 10px; display: flex; align-items: center; justify-content: center;
    margin-right: 23px; flex: none;
  }
  .contacts__text { font-size: 12px; color: var(--text-light); }

  .address {
    position: absolute; left: 562px; top: 424px;
    font-size: 11.5px; line-height: 18px; color: var(--text-grey);
    white-space: nowrap;
  }

  .values {
    position: absolute; left: 165px; top: 212px;
    transform: rotate(-31deg); transform-origin: left bottom;
    font-family: "Tinos", "Times New Roman", serif;
    font-size: 11.5px; letter-spacing: 0.5px; color: #fff; white-space: nowrap;
  }
  .back-tagline {
    position: absolute; left: 324px; top: 382px;
    font-size: 12px; line-height: 18px; color: var(--text-grey);
    white-space: nowrap;
  }
</style>
</head>
<body>

<section class="card card--front" aria-label="Business card front">
  <svg class="card__bands" viewBox="0 0 768 482" width="768" height="482" aria-hidden="true">
    <polygon points="572,0 768,0 768,314 467,482 0,482 0,346"/>
  </svg>
  <div class="brand">
    <span class="brand__square"></span>
    <span class="brand__name">Fennick Executive Search</span>
  </div>
  <p class="tagline-diagonal">Fennick Executive Search<br>Connecting Boards with Exceptional Leadership</p>
  <div class="holder">
    <p class="holder__name">Gordon <span class="holder__surname">Pellbury</span></p>
    <p class="holder__role">Managing Director</p>
  </div>
  <ul class="contacts">
    <li class="contacts__item"><span class="contacts__badge">T</span><span class="contacts__text">07823 906417, 0117 486 7132</span></li>
    <li class="contacts__item"><span class="contacts__badge">E</span><span class="contacts__text">gordon@fennickexecutive.co.uk</span></li>
    <li class="contacts__item"><span class="contacts__badge">w</span><span class="contacts__text">www.fennickexecutive.co.uk</span></li>
  </ul>
  <p class="address">58 Lindmoor Court, Hatherley Road,<br>Bristol, BS32 9QJ</p>
</section>

<section class="card card--back" aria-label="Business card back">
  <svg class="card__bands" viewBox="0 0 768 482" width="768" height="482" aria-hidden="true">
    <polygon points="0,0 571,0 0,346"/>
    <polygon points="768,314 768,482 466,482"/>
  </svg>
  <p class="values">ADVISE | ENGAGE | ELEVATE | ACHIEVE</p>
  <div class="brand">
    <span class="brand__square"></span>
    <span class="brand__name">Fennick Executive Search</span>
  </div>
  <p class="back-tagline">Fennick Executive Search,<br>Connecting Boards with Exceptional Leadership</p>
</section>

</body>
</html>
```